Torvane Center for Restorative Medicine

I need a full informational website for my medical practice. I would like to use my logo and also include a lot of emblems/pictures (also a picture of me in a white coat). The website should have a function for people to inquire and send me messages. I will be offering needle-less regenerative injection therapy, stem cell treatments, bioidentical hormone therapy, treatment for chronic illness, neurodegenerative diseases, skin rejuvenation, hair restoration, male enhancement, female enhancement, and anti-aging. The practice will not be accepting insurance and will be cash/credit card only.
A good example of written content and functionality is this website:
http://thebqvx.example/. However, I want different theme and tones.
Target Market(s)
High end clientele in Los Angeles, Southern California. Health minded people who are interested in living better and longer and can afford anti-aging treatments. Men and women who want to improve sexual health and wellbeing.
Industry/Entity Type
Medical And Science
Coding
Coded - Design and coding required
Number of Pages Required
5+ page
Font styles to use
Requirements
Must have
- 1. I will need to be able to move the site to other servers (needed for site speed)
- 2. Site must be build on WordPress
- 3. Full admin credentials for domain, cpanel, wordpress, ftp.
- 4. No third party interaction on development and content deployment once the site is on different servers
- 5. I will need the ability to add content and links to the site
- 6. I will need the ability to optimize the site for speed
- 7. I will need to ability to modify URLs so they are more SEO friendly
Nice to have
- pictures of stem cells, health improvement and regeneration, beauty, youthful individuals, older healthy and happy individuals. Medical designs.
Should not have
- flowers, dna

```html
<!DOCTYPE html>
<html lang="en">
<head>
<meta charset="utf-8">
<title>Torvane Center for Restorative Medicine</title>
<link rel="stylesheet" href="https://fonts.googleapis.com/css2?family=Montserrat:wght@400;500;600;700&family=Open+Sans:wght@400;600&display=swap">
<style>
:root{
  --navy:#1f3566;
  --navy-deep:#0b2454;
  --orange:#f7a21b;
  --blue:#3f8ad8;
  --text:#5b6472;
  --muted:#9aa2ad;
  --line:#dfe3e8;
  --tint:#eef2f6;
  --footer:#e6eef6;
  --white:#ffffff;
}
*{box-sizing:border-box;margin:0;padding:0}
html,body{width:1200px;height:2992px;overflow:hidden}
body{font-family:"Open Sans",Arial,sans-serif;color:var(--text);background:var(--white);position:relative}
h1,h2,h3,h4,.brand,.btn,.main-nav{font-family:"Montserrat",Arial,sans-serif}

/* header */
.site-header{position:absolute;top:0;left:0;width:1200px;height:72px;display:flex;align-items:center;justify-content:space-between;padding:0 52px 0 160px;background:var(--white)}
.brand{display:flex;align-items:center;gap:10px;color:var(--navy);font-weight:600;font-size:20px;letter-spacing:3px}
.brand-dot{width:26px;height:26px;border-radius:50%;background:var(--blue)}
.main-nav{display:flex;gap:22px;font-size:13px;font-weight:500;color:var(--navy)}

/* hero */
.hero{position:absolute;top:72px;left:0;width:1200px;height:528px;overflow:hidden}
.hero-visual{position:absolute;inset:0;
  background:linear-gradient(180deg,#f3f5f8 0%,#e2e8ef 26%,#7d9cc6 42%,#2f5595 58%,#12336c 78%,#0a1f48 100%)}
.hero-copy{position:relative;text-align:center;padding-top:46px}
.hero-copy h1{font-size:38px;line-height:44px;font-weight:700;color:var(--navy)}
.hero-copy p{width:520px;margin:14px auto 0;font-size:13px;line-height:19px;color:#4d5a6c}
.btn{display:inline-block;background:var(--orange);color:var(--white);font-size:12px;font-weight:600;padding:11px 26px;border-radius:2px}
.hero-copy .btn{margin-top:18px}

/* services */
.services{position:absolute;top:600px;left:0;width:1200px;height:560px;text-align:center}
.section-title{font-size:28px;font-weight:700;color:var(--navy)}
.services .section-title{margin-top:70px}
.title-rule{width:60px;height:3px;background:var(--orange);margin:12px auto 0}
.card-row{position:absolute;top:132px;left:44px;display:flex;gap:24px}
.service-card{width:205px;height:240px;background:var(--white);box-shadow:0 3px 12px rgba(20,40,80,.12);text-align:left}
.service-card h3{height:66px;padding:14px 12px 0;font-size:13px;line-height:18px;font-weight:600;color:var(--navy)}
.service-card .bar{height:3px;background:var(--orange);margin:0 12px 10px}
.service-card .media{height:150px;margin:0 12px}
.slider-arrow{position:absolute;top:222px;width:0;height:0;border-top:20px solid transparent;border-bottom:20px solid transparent}
.slider-arrow.prev{left:8px;border-right:18px solid #b9bfc7}
.slider-arrow.next{right:8px;border-left:18px solid #b9bfc7}
.services .btn{position:absolute;top:448px;left:526px}

/* welcome */
.welcome{position:absolute;top:1160px;left:0;width:1200px;height:600px;border-top:1px solid var(--line)}
.welcome-copy{position:absolute;left:180px;top:146px;width:470px}
.welcome-copy h2{font-size:28px;line-height:36px;font-weight:500;color:var(--navy)}
.welcome-copy h2 strong{font-weight:700}
.welcome-copy h4{margin-top:12px;font-size:14px;font-weight:500;color:var(--navy)}
.welcome-copy p{margin-top:16px;font-size:12px;line-height:19px}
.welcome-copy .btn{margin-top:22px}
.doctor-photo{position:absolute;left:688px;top:100px;width:276px;height:372px;background:linear-gradient(180deg,#e9edf1 0%,#d5dde5 55%,#f4f6f8 100%)}

/* testimonials */
.testimonials{position:absolute;top:1760px;left:0;width:1200px;height:420px;background:linear-gradient(180deg,var(--tint),#f6f8fa);text-align:center}
.testimonials .section-title{margin-top:60px;line-height:36px}
.quote-row{position:absolute;top:178px;left:104px;display:flex;gap:44px}
.quote-card{width:300px;height:184px;background:var(--white);box-shadow:0 3px 12px rgba(20,40,80,.1);padding:16px;text-align:left}
.quote-head{display:flex;align-items:center;gap:14px}
.avatar{width:66px;height:66px;background:linear-gradient(160deg,#c9b8a6,#6f7a8a)}
.quote-head h4{font-family:"Montserrat",Arial,sans-serif;font-size:13px;font-weight:600;color:var(--navy)}
.quote-head span{font-size:11px;color:var(--muted)}
.quote-card p{margin-top:14px;font-size:11px;line-height:17px}
.q-arrow{position:absolute;top:250px;width:0;height:0;border-top:16px solid transparent;border-bottom:16px solid transparent}
.q-arrow.prev{left:56px;border-right:14px solid #8fb6e2}
.q-arrow.next{right:56px;border-left:14px solid #8fb6e2}

/* contact */
.contact{position:absolute;top:2180px;left:0;width:1200px;height:560px;text-align:center}
.contact .section-title{margin-top:70px;font-size:32px;letter-spacing:1px}
.contact .lead{margin-top:6px;font-size:12px;color:var(--muted)}
.contact-form{position:absolute;top:182px;left:228px;width:744px;display:grid;grid-template-columns:320px 320px;column-gap:104px;row-gap:26px;text-align:left}
.field label{display:block;font-family:"Montserrat",Arial,sans-serif;font-size:10px;font-weight:600;color:var(--navy);letter-spacing:.5px}
.field .input{margin-top:8px;padding-bottom:8px;border-bottom:1px solid var(--line);font-size:11px;color:#b4bac2}
.field.wide{grid-column:1/3}
.contact .btn{position:absolute;top:468px;left:548px}

/* footer */
.site-footer{position:absolute;top:2740px;left:0;width:1200px;height:252px;background:var(--footer);text-align:center}
.site-footer .brand{justify-content:center;margin-top:30px;font-size:22px}
.footer-nav{display:flex;justify-content:center;gap:32px;margin-top:30px;font-family:"Montserrat",Arial,sans-serif;font-size:12px;font-weight:500;color:var(--navy)}
.legal{margin-top:18px;font-size:10px;color:var(--muted)}
.socials{display:flex;justify-content:center;gap:8px;margin-top:12px}
.socials span{width:22px;height:22px;border-radius:50%;background:var(--navy)}
.copyright{margin-top:12px;font-size:10px;color:var(--muted)}
</style>
</head>
<body>

<header class="site-header">
  <div class="brand"><span class="brand-dot"></span>TORVANE</div>
  <nav class="main-nav">
    <span>Home</span><span>About</span><span>Services</span><span>Science</span><span>Testimonials</span><span>Dr. Vale Videos</span><span>Contact</span>
  </nav>
</header>

<section class="hero">
  <div class="hero-visual" role="img" aria-label="Hero image of glowing nerve cells on a deep blue background"></div>
  <div class="hero-copy">
    <h1>Torvane center is the medicine<br>of the future.</h1>
    <p>We customize our services to meet the diverse needs of patients, restore vitality and support lifelong wellness.</p>
    <span class="btn">Inquire Now</span>
  </div>
</section>

<section class="services">
  <h2 class="section-title">Our Services</h2>
  <div class="title-rule"></div>
  <span class="slider-arrow prev"></span>
  <div class="card-row">
    <article class="service-card"><h3>Needleless regenerative injection therapy</h3><div class="bar"></div><div class="media" role="img" aria-label="Woman touching her smooth cheek" style="background:linear-gradient(160deg,#f1ddd0,#c99a86)"></div></article>
    <article class="service-card"><h3>Stem Cell Treatments</h3><div class="bar"></div><div class="media" role="img" aria-label="Stem cells under a microscope" style="background:linear-gradient(160deg,#8f7fe0,#2c2590)"></div></article>
    <article class="service-card"><h3>Treatment for chronic illness</h3><div class="bar"></div><div class="media" role="img" aria-label="Person holding a painful shoulder" style="background:linear-gradient(160deg,#f6f3f1,#d9b8a7)"></div></article>
    <article class="service-card"><h3>Hair Restoration</h3><div class="bar"></div><div class="media" role="img" aria-label="Woman with long healthy hair" style="background:linear-gradient(160deg,#e8e2dd,#8a6a55)"></div></article>
    <article class="service-card"><h3>Neurodegenerative Diseases</h3><div class="bar"></div><div class="media" role="img" aria-label="Brain scan images" style="background:linear-gradient(160deg,#6e6e6e,#1c1c1c)"></div></article>
  </div>
  <span class="slider-arrow next"></span>
  <span class="btn">More Services</span>
</section>

<section class="welcome">
  <div class="welcome-copy">
    <h2>Welcome to <strong>Torvane center for restorative medicine</strong></h2>
    <h4>CEO of Torvane center for restorative medicine</h4>
    <p>Our physicians combine modern regenerative science with personal attention to help each patient restore function and vitality. Every plan begins with a thorough consultation, careful diagnostics and clear goals. We treat the causes behind chronic conditions, not only the symptoms, so our patients can live better and longer.</p>
    <span class="btn">Meet the Doctor</span>
  </div>
  <div class="doctor-photo" role="img" aria-label="Doctor in a white coat with a stethoscope"></div>
</section>

<section class="testimonials">
  <h2 class="section-title">Don't believe us?<br>Hear from our customers</h2>
  <span class="q-arrow prev"></span>
  <div class="quote-row">
    <article class="quote-card">
      <div class="quote-head"><div class="avatar" role="img" aria-label="Portrait of patient Daniel Hart"></div><div><h4>Daniel Hart</h4><span>Patient</span></div></div>
      <p>After three months of treatment I feel stronger and more rested than I have in years. The team is warm and thorough.</p>
    </article>
    <article class="quote-card">
      <div class="quote-head"><div class="avatar" role="img" aria-label="Portrait of patient Marcus Lee"></div><div><h4>Marcus Lee</h4><span>Patient</span></div></div>
      <p>The care here is personal and unhurried. My joints move freely again and my energy has returned to what it once was.</p>
    </article>
    <article class="quote-card">
      <div class="quote-head"><div class="avatar" role="img" aria-label="Portrait of patient Robert Kane"></div><div><h4>Robert Kane</h4><span>Patient</span></div></div>
      <p>Clear answers, kind staff and real results. I recommend this center to anyone who wants to age with strength and ease.</p>
    </article>
  </div>
  <span class="q-arrow next"></span>
</section>

<section class="contact">
  <h2 class="section-title">CONTACT US</h2>
  <p class="lead">Fill out the form below</p>
  <div class="contact-form">
    <div class="field"><label>FIRST NAME</label><div class="input">Enter your first name</div></div>
    <div class="field"><label>LAST NAME</label><div class="input">Enter your last name</div></div>
    <div class="field"><label>EMAIL ADDRESS</label><div class="input">Enter your email address</div></div>
    <div class="field"><label>PHONE NUMBER</label><div class="input">Enter your phone number</div></div>
    <div class="field wide"><label>NOTES</label><div class="input">Write your message here</div></div>
  </div>
  <span class="btn">Submit Now</span>
</section>

<footer class="site-footer">
  <div class="brand"><span class="brand-dot"></span>TORVANE</div>
  <nav class="footer-nav"><span>Home</span><span>About</span><span>Services</span><span>Science</span><span>Testimonials</span><span>Dr. Vale Videos</span><span>Contact</span></nav>
  <p class="legal">Terms of Use | Privacy Policy | Sitemap</p>
  <div class="socials"><span></span><span></span><span></span><span></span></div>
  <p class="copyright">Copyright © 2024 Torvane Center for Restorative Medicine. All Rights Reserved.</p>
</footer>

</body>
</html>
```